Design athlete website layout

We're looking to design a contemporary website page that features an athlete. We have a basic layout but feel it needs some pop. 1. We would like ideas on how to make the buttons more interesting with a hint of color or transparent text, etc... However, we do prefer a simple look with black and white. 2. We would like to have the athlete's name appear with an interesting feature (transparency or other ideas) on the photo (Hero photo). The photos at the top, including the existing Hero pic will carousel (4 photo's). 3. We like the current tool bar but we would like to see if there's anything you would add to create a more interesting look. The final design should be a beautiful and organized visual representation of the athlete.
Number of Pages Required
1 page
Look and feel
Each slider illustrates characteristics of the customer's brand and the style your logo design should communicate.

```html
<!DOCTYPE html>
<html lang="en">
<head>
<meta charset="utf-8">
<title>Marlowe — Athlete</title>
<link href="https://fonts.googleapis.com/css2?family=Rufina:wght@400;700&family=Raleway:wght@400;600;700&display=swap" rel="stylesheet">
<style>
:root{
  --ink:#0b0b0b;
  --night:#151a1f;
  --white:#ffffff;
  --accent:#f26b2a;
  --grey:#7a7a7a;
  --line:#d9d9d9;
  --serif:"Rufina", Georgia, serif;
  --sans:"Raleway", Arial, sans-serif;
}
*{margin:0;padding:0;box-sizing:border-box}
html,body{width:1200px;height:3169px;overflow:hidden;background:var(--white)}
body{position:relative;font-family:var(--sans);color:var(--ink)}
.abs{position:absolute}
.btn{position:absolute;display:flex;align-items:center;justify-content:center;font-family:var(--sans);font-size:11px;font-weight:600;letter-spacing:.5px;text-transform:uppercase;color:var(--white);background:var(--accent);text-decoration:none}

/* hero */
.hero{position:absolute;left:0;top:0;width:1200px;height:740px;overflow:hidden}
.hero svg{position:absolute;inset:0}
.brand{position:absolute;left:44px;top:28px;font-family:var(--serif);font-size:30px;color:var(--white)}
.nav{position:absolute;top:44px;left:0;width:1200px;height:24px}
.nav a{position:absolute;font-family:var(--sans);font-size:14px;font-weight:700;color:var(--white);text-decoration:none}
.nav a.active{color:var(--accent);border-bottom:2px solid var(--accent);padding-bottom:8px}
.hero-title{position:absolute;left:106px;top:282px;font-family:var(--serif);font-size:68px;letter-spacing:3px;color:var(--white)}
.hero-text{position:absolute;left:110px;top:370px;width:660px;font-size:15.5px;line-height:22px;color:var(--white)}
.hero-btn{left:110px;top:484px;width:152px;height:57px;background:var(--ink);font-size:12px}
.social{position:absolute;top:608px;width:110px;text-align:center;color:var(--white);font-family:var(--serif);font-size:19px}
.social .dot{width:64px;height:64px;border-radius:50%;background:var(--white);margin:0 auto 14px}

/* welcome */
.welcome-title{position:absolute;top:818px;left:0;width:1200px;text-align:center;font-family:var(--serif);font-size:29px;letter-spacing:1px}
.welcome-title span{color:var(--accent)}
.welcome-rule{position:absolute;top:838px;height:1px;background:var(--line)}
.welcome-text{position:absolute;top:878px;left:130px;width:940px;text-align:center;font-size:14px;line-height:24px;color:var(--grey)}

/* features */
.features{position:absolute;left:0;top:972px;width:1200px;height:1363px}
.features svg{position:absolute;inset:0}
.feature{position:absolute;width:560px;color:var(--white)}
.feature h3{font-family:var(--serif);font-weight:400;font-size:23px;color:var(--accent);margin-bottom:10px}
.feature p{font-size:13.5px;line-height:20px}
.feature.right{text-align:right;right:48px}
.feature.left{left:47px}
.feature .btn{position:relative;display:inline-flex;width:121px;height:38px;margin-top:24px}

/* gallery */
.gallery-title{position:absolute;top:2382px;left:0;width:1200px;text-align:center;font-family:var(--serif);font-size:29px;color:var(--accent)}
.tile{position:absolute;top:2457px;width:263px;height:254px}
.tile-caption{position:absolute;inset:0;background:rgba(10,10,10,.78);color:var(--white);text-align:center;padding-top:48px}
.tile-caption h4{font-family:var(--serif);font-size:15px;color:var(--accent);margin-bottom:12px}
.tile-caption p{font-size:13px;line-height:17px;padding:0 28px}
.tile-caption .btn{position:relative;display:inline-flex;width:100px;height:28px;margin-top:10px}
.pager{position:absolute;top:2736px;width:10px;height:10px;border-radius:50%;border:1.5px solid var(--accent)}
.pager.on{background:var(--accent)}

/* footer */
.footer{position:absolute;left:0;top:2804px;width:1200px;height:365px;background:#000}
.footer svg{position:absolute;inset:0}
.contact-title{position:absolute;left:47px;top:58px;font-family:var(--serif);font-size:22px;color:var(--accent)}
.contact-lines{position:absolute;left:50px;top:96px;font-size:14px;line-height:24.5px;color:var(--white)}
.copyright{position:absolute;top:313px;left:0;width:1184px;text-align:center;font-family:var(--serif);font-size:11px;color:var(--grey)}
.foot-social{position:absolute;top:298px;width:28px;height:28px;border:2px solid var(--accent);background:var(--accent)}
.foot-social.dark{background:#000}
</style>
</head>
<body>

<header class="hero">
  <svg width="1200" height="740" viewBox="0 0 1200 740">
    <defs>
      <linearGradient id="heroGrad" x1="0" y1="0" x2="1" y2="0">
        <stop offset="0" stop-color="#3a3f44"/>
        <stop offset=".45" stop-color="#26313a"/>
        <stop offset="1" stop-color="#16252c"/>
      </linearGradient>
    </defs>
    <rect width="1200" height="740" fill="url(#heroGrad)" role="img" aria-label="Hero photo: tennis player mid-swing with racket on court"/>
    <rect width="1200" height="740" fill="rgba(0,0,0,.25)"/>
    <polygon points="0,740 0,690 1200,500 1200,740" fill="rgba(0,0,0,.72)"/>
    <circle cx="53" cy="410" r="19" fill="#fff" opacity=".9"/>
    <path d="M57 402 L49 410 L57 418" fill="none" stroke="#222" stroke-width="2.5"/>
    <circle cx="1145" cy="415" r="19" fill="#fff" opacity=".9"/>
    <path d="M1141 407 L1149 415 L1141 423" fill="none" stroke="#222" stroke-width="2.5"/>
  </svg>
  <div class="brand">Marlowe</div>
  <nav class="nav">
    <a class="active" href="#" style="left:472px">Marlowe</a>
    <a href="#" style="left:575px">Blog</a>
    <a href="#" style="left:663px">Gallery</a>
    <a href="#" style="left:770px">Video</a>
    <a href="#" style="left:866px">News</a>
    <a href="#" style="left:962px">Foundation</a>
    <a href="#" style="left:1094px">Schedule</a>
  </nav>
  <h1 class="hero-title">MARLOWE</h1>
  <p class="hero-text">Lorem ipsum dolor sit amet, consectetur adipiscing elit, sed do eiusmod tempor incididunt ut labore et dolore magna aliqua. Ut enim ad minim veniam, quis nostrud exercitation ullamco laboris nisi ut aliquip ex ea commodo consequat. Duis aute irure dolor in reprehenderit in voluptate velit esse cillum</p>
  <a class="btn hero-btn" href="#">Read More</a>
  <div class="social" style="left:801px"><div class="dot"></div>Friendbook</div>
  <div class="social" style="left:911px"><div class="dot"></div>Chirper</div>
  <div class="social" style="left:1023px"><div class="dot"></div>Linkline</div>
</header>

<section>
  <div class="welcome-rule" style="left:47px;width:380px"></div>
  <div class="welcome-rule" style="left:786px;width:366px"></div>
  <h2 class="welcome-title">WELCOME TO <span>NAME</span></h2>
  <p class="welcome-text">Welcome to the home of Harbor Auto Lane – simply the best at helping you locate and purchase your next vehicle, if you are looking for a modern exotic, sports car, collectible or classic.</p>
</section>

<section class="features">
  <svg width="1200" height="1363" viewBox="0 0 1200 1363">
    <defs>
      <linearGradient id="featGrad" x1="0" y1="0" x2="0" y2="1">
        <stop offset="0" stop-color="#2b2f33"/>
        <stop offset=".35" stop-color="#3a2d33"/>
        <stop offset=".65" stop-color="#23282e"/>
        <stop offset="1" stop-color="#1c2a36"/>
      </linearGradient>
    </defs>
    <rect width="1200" height="1363" fill="url(#featGrad)" role="img" aria-label="Montage of tennis photos: athlete smiling, lifting a trophy and playing on court"/>
    <rect width="1200" height="1363" fill="rgba(0,0,0,.35)"/>
    <g stroke="#fff" stroke-width="4" fill="none">
      <line x1="0" y1="4" x2="1200" y2="391"/>
      <line x1="0" y1="592" x2="1200" y2="380"/>
      <line x1="0" y1="608" x2="1200" y2="961"/>
      <line x1="0" y1="1357" x2="1200" y2="993"/>
    </g>
  </svg>
  <div class="feature right" style="top:50px"><h3>Blog</h3><p>Lorem ipsum dolor sit amet, consectetur adipiscing elit, sed do eiusmod tempor incididunt ut labore et dolore magna aliqua. Ut enim ad minim veniam, quis nostrud exercitation ullamco laboris nisi ut aliquip ex ea commodo consequat. Duis aute irure dolor in reprehenderit in voluptate velit esse cillum dolore eu fugiat nulla pariatur.</p><a class="btn" href="#">View All</a></div>
  <div class="feature left" style="top:258px"><h3>News</h3><p>Lorem ipsum dolor sit amet, consectetur adipiscing elit, sed do eiusmod tempor incididunt ut labore et dolore magna aliqua. Ut enim ad minim veniam, quis nostrud exercitation ullamco laboris nisi ut aliquip ex ea commodo consequat. Duis aute irure dolor in reprehenderit in voluptate velit esse cillum dolore eu fugiat nulla pariatur.</p><a class="btn" href="#">View All</a></div>
  <div class="feature right" style="top:559px"><h3>Video</h3><p>Lorem ipsum dolor sit amet, consectetur adipiscing elit, sed do eiusmod tempor incididunt ut labore et dolore magna aliqua. Ut enim ad minim veniam, quis nostrud exercitation ullamco laboris nisi ut aliquip ex ea commodo consequat. Duis aute irure dolor in reprehenderit in voluptate velit esse cillum dolore eu fugiat nulla pariatur.</p><a class="btn" href="#">View All</a></div>
  <div class="feature left" style="top:909px"><h3>Foundation</h3><p>Lorem ipsum dolor sit amet, consectetur adipiscing elit, sed do eiusmod tempor incididunt ut labore et dolore magna aliqua. Ut enim ad minim veniam, quis nostrud exercitation ullamco laboris nisi ut aliquip ex ea commodo consequat. Duis aute irure dolor in reprehenderit in voluptate velit esse cillum dolore eu fugiat nulla pariatur.</p><a class="btn" href="#">View All</a></div>
  <div class="feature right" style="top:1180px;width:470px"><h3>Grand Lawn Championship</h3><p>Lorem ipsum dolor sit amet, consectetur adipiscing elit, sed do eiusmod tempor incididunt sit amet, consectetur adipiscing elit, sed do eiusmod tempor incididunt ut labore et dolore magna aliqua.labore et dolore magna.</p><a class="btn" href="#" style="margin-top:12px">View All</a></div>
</section>

<section>
  <h2 class="gallery-title">OUR GALLERY</h2>
  <div class="tile" style="left:47px;background:linear-gradient(160deg,#b8a48e,#6d5a4a)" role="img" aria-label="Photo: athlete in white celebrating with a raised fist"></div>
  <div class="tile" style="left:328px;background:linear-gradient(160deg,#6a7480,#3a4048)" role="img" aria-label="Photo: athlete waving to the crowd">
    <div class="tile-caption"><h4>LOREM IPSUM DOLOR</h4><p>Lorem ipsum dolor amet, consectetur adipiscing elit, sed do eiusmod sed do tempor</p><a class="btn" href="#">View</a></div>
  </div>
  <div class="tile" style="left:609px;background:linear-gradient(160deg,#8a4f6a,#c2453c)" role="img" aria-label="Photo: two players shaking hands at the net"></div>
  <div class="tile" style="left:890px;background:linear-gradient(160deg,#5b8a70,#2f4d44)" role="img" aria-label="Photo: athlete in a teal visor on court"></div>
  <span class="pager" style="left:580px"></span>
  <span class="pager on" style="left:597px"></span>
  <span class="pager" style="left:614px"></span>
</section>

<footer class="footer">
  <svg width="1200" height="365" viewBox="0 0 1200 365">
    <line x1="0" y1="313" x2="1200" y2="2" stroke="#fff" stroke-width="3"/>
  </svg>
  <h3 class="contact-title">Contact Us</h3>
  <p class="contact-lines">Address Line1, Address Line 2,<br>Lorem ipsum dolor sit.<br>Country &nbsp;- 123456</p>
  <p class="copyright">Copyright 2016 Company Name All Rights Reserved.</p>
  <span class="foot-social dark" style="left:1001px"></span>
  <span class="foot-social" style="left:1039px"></span>
  <span class="foot-social" style="left:1077px"></span>
  <span class="foot-social dark" style="left:1115px"></span>
</footer>

</body>
</html>
```